Wim pod OBR is the name of my childrens book for middle school kids. I'm looking to get a book cover

I'm looking to get an interesting book cover for the book I'm working on called Wim OBR. It is a book about a middle school kid and his family and friends.It is first one. in a series of books.The book size is 8 1/2 x 5 1/2 .The book is written like a diary much like Scraps of a gloomy sprout or Fizzle Capers. It should have the look and feel of a diary or journal. For this first book I wanted to use yellow or gold color for the cover. But if you have a better Idea go for it! I already have a logo which I'll upload for your review which has to go on the cover. I'm looking for unusual and different ideas so please be as creative as you want to be. Thanks

Target Market(s)

Middle school kids ages 9 to 12

Industry/Entity Type

School

Font styles to use
Serif

Colors
ffcf3e
ffc214
ec1f27
f04a51
0456a4
3176b5
85acd3
9ccb3b
acd136

Requirements
Must have
• My Logo ( which is the title of the book. Wim Pod OBR) I Uploaded it. The Subtitle: Chasing clouds and Counting Pebbles. Main character on the cover. I uploaded two different versions of main characters. Please use either one. Please redraw if necessary.
Nice to have
• Maybe look like a Diary or journal with lock and key or combination lock or different type of diary. But doesn't have to look like that.
Should not have
• The Flag, Stars and stripes,

```html
<!DOCTYPE html>
<html lang="en">
<head>
<meta charset="utf-8">
<title>Wim Pod OBR – Chasing Clouds and Counting Pebbles</title>
<link rel="stylesheet" href="https://fonts.googleapis.com/css2?family=Permanent+Marker&display=swap">
<style>
  :root {
    --cover-green: #9acb3c;
    --title-blue: #0456a4;
    --journal-brown: #3a2510;
    --wall-blue: #3a72b6;
    --floor-blue: #0b55a5;
    --floor-deep: #0a4a92;
    --horizon-grey: #a8adb3;
    --board-green: #0c7a1c;
    --board-frame: #b08a4a;
    --chalk: #f4f6f2;
    --spiral: #84bd3a;
    --tab-green: #8cbf2e;
    --tab-red: #a0141c;
    --tab-mid-green: #2f9a2a;
    --tab-maroon: #6a0f2a;
    --mark-red: #d02a2e;
    --hero-green: #9ccb3b;
    --hero-yellow: #ffc214;
  }
  html, body {
    margin: 0;
    padding: 0;
    width: 800px;
    height: 1200px;
    overflow: hidden;
    background: var(--cover-green);
  }
  .cover {
    position: relative;
    width: 800px;
    height: 1200px;
    background: var(--cover-green);
    font-family: "Permanent Marker", cursive;
  }
  .series-title {
    position: absolute;
    top: 58px;
    left: 0;
    width: 800px;
    margin: 0;
    text-align: center;
    white-space: nowrap;
    font-size: 104px;
    font-weight: 400;
    line-height: 1.2;
    color: var(--title-blue);
  }
  .journal {
    position: absolute;
    left: 90px;
    top: 238px;
    width: 648px;
    height: 894px;
    background: var(--journal-brown);
    border-radius: 34px;
    box-shadow: 0 6px 22px rgba(40, 60, 10, 0.45);
  }
  .journal-tab {
    position: absolute;
    left: 738px;
    width: 14px;
    border-radius: 0 6px 6px 0;
  }
  .tab-1 { top: 312px; height: 186px; background: var(--tab-green); }
  .tab-2 { top: 502px; height: 94px; background: var(--tab-red); }
  .tab-3 { top: 600px; height: 100px; background: var(--tab-mid-green); }
  .tab-4 { top: 702px; height: 70px; background: var(--tab-maroon); }
  .page-scene {
    position: absolute;
    left: 148px;
    top: 280px;
    width: 556px;
    height: 812px;
    border-radius: 0 44px 0 0;
    overflow: hidden;
    background: linear-gradient(to bottom, var(--wall-blue) 0%, var(--wall-blue) 52%, var(--floor-blue) 52.2%, var(--floor-deep) 100%);
  }
  .horizon-line {
    position: absolute;
    left: 226px;
    top: 751px;
    width: 410px;
    height: 2px;
    background: var(--horizon-grey);
  }
  .chalkboard {
    position: absolute;
    left: 190px;
    top: 310px;
    width: 468px;
    height: 330px;
    box-sizing: border-box;
    border: 8px solid var(--board-frame);
    background: var(--board-green);
    box-shadow: 0 4px 10px rgba(0, 0, 0, 0.45);
    padding-top: 24px;
  }
  .chalkboard-ledge {
    position: absolute;
    left: 328px;
    top: 636px;
    width: 206px;
    height: 12px;
    background: var(--board-frame);
  }
  .subtitle {
    margin: 0;
    color: var(--chalk);
    font-size: 44px;
    font-weight: 400;
    line-height: 71px;
    text-transform: uppercase;
    text-align: center;
    white-space: nowrap;
  }
  .main-character {
    position: absolute;
    left: 304px;
    top: 656px;
    width: 272px;
    height: 376px;
    border-radius: 120px 120px 24px 24px;
    background: linear-gradient(to bottom, var(--chalk) 0%, var(--hero-green) 45%, var(--hero-yellow) 75%, var(--floor-blue) 100%);
    opacity: 0.9;
  }
  .spiral {
    position: absolute;
    left: 58px;
    top: 310px;
  }
  .series-mark {
    position: absolute;
    left: 412px;
    top: 1004px;
    width: 300px;
    margin: 0;
    text-align: right;
    white-space: nowrap;
    font-size: 48px;
    font-weight: 400;
    line-height: 1.4;
    color: var(--mark-red);
  }
</style>
</head>
<body>
  <main class="cover">
    <h1 class="series-title">Wim Pod OBR</h1>

    <div class="journal"></div>
    <div class="journal-tab tab-1"></div>
    <div class="journal-tab tab-2"></div>
    <div class="journal-tab tab-3"></div>
    <div class="journal-tab tab-4"></div>

    <div class="page-scene"></div>
    <div class="horizon-line"></div>

    <div class="chalkboard">
      <p class="subtitle">Chasing Clouds<br>and<br>Counting Pebbles</p>
    </div>
    <div class="chalkboard-ledge"></div>

    <div class="main-character" role="img" aria-label="Main character: a thoughtful middle school boy in a green shirt and blue cap, sitting at a yellow school desk with a pencil behind his ear"></div>

    <svg class="spiral" width="84" height="730" viewBox="0 0 84 730" aria-hidden="true">
      <g fill="none" stroke="var(--spiral)" stroke-width="6">
        <ellipse cx="42" cy="12" rx="36" ry="9"/>
        <ellipse cx="42" cy="35" rx="36" ry="9"/>
        <ellipse cx="42" cy="58" rx="36" ry="9"/>
        <ellipse cx="42" cy="81" rx="36" ry="9"/>
        <ellipse cx="42" cy="104" rx="36" ry="9"/>
        <ellipse cx="42" cy="127" rx="36" ry="9"/>
        <ellipse cx="42" cy="150" rx="36" ry="9"/>
        <ellipse cx="42" cy="173" rx="36" ry="9"/>
        <ellipse cx="42" cy="196" rx="36" ry="9"/>
        <ellipse cx="42" cy="219" rx="36" ry="9"/>
        <ellipse cx="42" cy="242" rx="36" ry="9"/>
        <ellipse cx="42" cy="265" rx="36" ry="9"/>
        <ellipse cx="42" cy="288" rx="36" ry="9"/>
        <ellipse cx="42" cy="311" rx="36" ry="9"/>
        <ellipse cx="42" cy="334" rx="36" ry="9"/>
        <ellipse cx="42" cy="357" rx="36" ry="9"/>
        <ellipse cx="42" cy="380" rx="36" ry="9"/>
        <ellipse cx="42" cy="403" rx="36" ry="9"/>
        <ellipse cx="42" cy="426" rx="36" ry="9"/>
        <ellipse cx="42" cy="449" rx="36" ry="9"/>
        <ellipse cx="42" cy="472" rx="36" ry="9"/>
        <ellipse cx="42" cy="495" rx="36" ry="9"/>
        <ellipse cx="42" cy="518" rx="36" ry="9"/>
        <ellipse cx="42" cy="541" rx="36" ry="9"/>
        <ellipse cx="42" cy="564" rx="36" ry="9"/>
        <ellipse cx="42" cy="587" rx="36" ry="9"/>
        <ellipse cx="42" cy="610" rx="36" ry="9"/>
        <ellipse cx="42" cy="633" rx="36" ry="9"/>
        <ellipse cx="42" cy="656" rx="36" ry="9"/>
        <ellipse cx="42" cy="679" rx="36" ry="9"/>
        <ellipse cx="42" cy="702" rx="36" ry="9"/>
      </g>
    </svg>

    <p class="series-mark">Wim Pod OBR</p>
  </main>
</body>
</html>
```